Business Card - Cooperate

Business Card for Larkfield Management Consulting

Target Market(s)

Corparte - b2B

Industry/Entity Type

Management Consulting - Professional Services

Contact Information for Business Card

Company Name , Slogan , Dummy Address,

Requirements
Must have
• Reach your Full Potential

```html
<!DOCTYPE html>
<html lang="en">
<head>
<meta charset="utf-8">
<title>Larkfield Management Consulting – Business Card</title>
<link rel="stylesheet" href="https://fonts.googleapis.com/css2?family=Open+Sans:wght@400;700;800&display=swap">
<style>
  :root {
    --stage: #141414;
    --card-green: #32c012;
    --card-white: #ffffff;
    --navy: #1f1a6e;
    --royal: #0a4fd6;
    --sky: #0a7cff;
    --lime: #7ad81e;
    --teal: #14a38a;
    --grey-text: #6f6f6f;
    --icon-green: #5cc61a;
  }
  * { margin: 0; padding: 0; box-sizing: border-box; }
  html, body { width: 1200px; height: 849px; overflow: hidden; }
  body {
    background: var(--stage);
    font-family: "Open Sans", Arial, sans-serif;
    display: flex;
    align-items: center;
    justify-content: center;
    gap: 40px;
  }
  .card {
    position: relative;
    width: 540px;
    height: 310px;
    overflow: hidden;
    box-shadow: 0 18px 40px rgba(0,0,0,.55);
  }
  .card--front { background: var(--card-green); }
  .card--back { background: var(--card-white); }

  .decor {
    position: absolute;
    left: 0;
    bottom: 0;
    width: 250px;
    height: 100%;
    border-radius: 0 140px 140px 0;
  }
  .card--front .decor {
    background: linear-gradient(160deg, var(--navy) 0%, var(--sky) 45%, var(--teal) 75%, var(--card-green) 100%);
  }
  .card--back .decor {
    background: linear-gradient(160deg, var(--navy) 0%, var(--sky) 40%, var(--teal) 70%, var(--lime) 100%);
  }

  .brand {
    position: absolute;
    right: 34px;
    text-align: left;
  }
  .card--front .brand { top: 110px; }
  .card--back .brand { top: 36px; }
  .brand__name {
    font-weight: 800;
    font-size: 46px;
    line-height: 1;
    letter-spacing: -0.5px;
  }
  .card--front .brand__name { color: var(--navy); }
  .card--back .brand__name { color: var(--royal); }
  .brand__slogan {
    margin-top: 6px;
    font-weight: 800;
    font-size: 10.5px;
    letter-spacing: 2.6px;
    text-transform: uppercase;
  }
  .card--front .brand__slogan { color: var(--navy); }
  .card--back .brand__slogan { color: var(--teal); }

  .person {
    position: absolute;
    left: 30px;
    top: 128px;
    color: #fff;
  }
  .person__name { font-weight: 700; font-size: 20px; line-height: 1.2; }
  .person__role { font-size: 11px; opacity: .9; }

  .contact {
    position: absolute;
    left: 290px;
    top: 150px;
    list-style: none;
    color: var(--grey-text);
    font-size: 12.5px;
    line-height: 1.35;
  }
  .contact__item { display: flex; align-items: flex-start; gap: 9px; margin-bottom: 10px; }
  .contact__icon { flex: none; width: 14px; height: 14px; margin-top: 2px; }
</style>
</head>
<body>

  <section class="card card--front" aria-label="Card front">
    <div class="decor" role="img" aria-label="Brand swirl decoration in navy, blue and green"></div>
    <div class="brand">
      <div class="brand__name">Larkfield</div>
      <div class="brand__slogan">Reach your full potential</div>
    </div>
  </section>

  <section class="card card--back" aria-label="Card back">
    <div class="decor" role="img" aria-label="Brand swirl decoration in navy, blue and green"></div>
    <div class="person">
      <div class="person__name">Dana Mercer</div>
      <div class="person__role">General Contractor</div>
    </div>
    <div class="brand">
      <div class="brand__name">Larkfield</div>
      <div class="brand__slogan">Reach your full potential</div>
    </div>
    <ul class="contact">
      <li class="contact__item">
        <svg class="contact__icon" viewBox="0 0 14 14" aria-hidden="true">
          <path d="M7 1a4.5 4.5 0 0 0-4.5 4.5C2.5 9 7 13 7 13s4.5-4 4.5-7.5A4.5 4.5 0 0 0 7 1z" fill="var(--icon-green)"/>
          <circle cx="7" cy="5.5" r="1.7" fill="#fff"/>
        </svg>
        <span>218 Harlow Bend Road<br>Millbrook, SC 29140</span>
      </li>
      <li class="contact__item">
        <svg class="contact__icon" viewBox="0 0 14 14" aria-hidden="true">
          <circle cx="7" cy="7" r="6.5" fill="var(--icon-green)"/>
          <path d="M4.6 4.2l1.3-.3.8 1.6-.8.6a4.5 4.5 0 0 0 2 2l.6-.8 1.6.8-.3 1.3c-3 .2-5.4-2.2-5.2-5.2z" fill="#fff"/>
        </svg>
        <span>011 480 5721</span>
      </li>
      <li class="contact__item">
        <svg class="contact__icon" viewBox="0 0 14 14" aria-hidden="true">
          <circle cx="7" cy="7" r="6.5" fill="var(--icon-green)"/>
          <rect x="3.6" y="4.6" width="6.8" height="4.8" rx=".6" fill="#fff"/>
          <path d="M3.8 4.9L7 7.3l3.2-2.4" stroke="var(--icon-green)" stroke-width=".9" fill="none"/>
        </svg>
        <span>hello@larkfieldconsult.com</span>
      </li>
    </ul>
  </section>

</body>
</html>
```